TRV business card

Need a business card for a company that provides instructional design and elearning development services. The website is here: http://tarvexa.studio/

I'm attaching a current logo, as well as the old business card design. While I like to keep it clean, the old design is too simplistic for my liking. The only idea I want to reuse from the old design is placing industry jargon on the back of the card, just need a better way to present it. But if you have other ideas for the back--feel free to experiment.

Please use the colors complementary to the color we have on the website. Thank you!

```html
<!DOCTYPE html>
<html lang="en">
<head>
<meta charset="utf-8">
<title>TRV Business Card</title>
<link href="https://fonts.googleapis.com/css2?family=Source+Sans+3:wght@400;600;700&display=swap" rel="stylesheet">
<style>
  :root {
    --teal: #00b1b0;
    --gold: #d9cc98;
    --gold-text: #cfc08a;
    --white: #ffffff;
    --paper: #f7f7f5;
    --backdrop: #ecebe7;
  }
  * { box-sizing: border-box; margin: 0; padding: 0; }
  html, body { width: 1200px; height: 900px; overflow: hidden; }
  body {
    background: var(--backdrop);
    font-family: "Source Sans 3", "Segoe UI", sans-serif;
    position: relative;
  }
  .card {
    position: absolute;
    width: 560px;
    height: 320px;
    background: linear-gradient(180deg, var(--white), var(--paper));
    box-shadow: 0 10px 24px rgba(0,0,0,0.18);
    overflow: hidden;
  }
  .card--back { left: 110px; top: 100px; }
  .card--front { left: 530px; top: 470px; }

  .card__band {
    position: absolute;
    left: 0; right: 0; bottom: 0;
    height: 178px;
    background: var(--teal);
    border-top: 6px solid var(--gold);
  }

  .brand {
    position: absolute;
    top: 48px; left: 0; right: 0;
    display: flex;
    align-items: center;
    justify-content: center;
    gap: 14px;
  }
  .brand__mark {
    width: 34px; height: 34px;
    background: var(--teal);
  }
  .brand__name {
    font-weight: 600;
    font-size: 42px;
    color: var(--gold-text);
    letter-spacing: 0.5px;
  }

  .services {
    position: absolute;
    left: 0; right: 0; top: 22px;
    text-align: center;
    color: var(--white);
  }
  .services__title {
    font-weight: 600;
    font-size: 19px;
    letter-spacing: 0.6px;
    margin-bottom: 14px;
  }
  .services__row {
    font-weight: 600;
    font-size: 16px;
    line-height: 30px;
  }
  .services__dot {
    display: inline-block;
    width: 7px; height: 7px;
    border-radius: 50%;
    background: var(--white);
    margin: 0 12px;
    vertical-align: middle;
  }

  .contact {
    position: absolute;
    left: 200px; right: 20px; top: 18px;
    text-align: center;
    color: var(--white);
    font-size: 16px;
    line-height: 22px;
  }
  .contact__name {
    font-weight: 700;
    font-size: 20px;
    margin-bottom: 16px;
  }
  .contact__label { font-weight: 700; }
</style>
</head>
<body>

  <section class="card card--back" aria-label="Card back">
    <div class="brand">
      <span class="brand__mark"></span>
      <span class="brand__name">Tarvexa Studio</span>
    </div>
    <div class="card__band">
      <div class="services">
        <h2 class="services__title">HOW CAN WE HELP?</h2>
        <p class="services__row">Mobile Learning Scorm<span class="services__dot"></span>Instructional Design Lms</p>
        <p class="services__row">Moocs Elearning Html5<span class="services__dot"></span>Adult Learning Theory</p>
        <p class="services__row">Gamification Classroom<span class="services__dot"></span>Xapi Blended Learning</p>
      </div>
    </div>
  </section>

  <section class="card card--front" aria-label="Card front">
    <div class="brand">
      <span class="brand__mark"></span>
      <span class="brand__name">Tarvexa Studio</span>
    </div>
    <div class="card__band">
      <div class="contact">
        <h1 class="contact__name">Marcus Elwood</h1>
        <p><span class="contact__label">Phone:</span> 555-014-2290</p>
        <p><span class="contact__label">Email:</span> melwood@tarvexa.studio</p>
        <p><span class="contact__label">Website:</span> www.tarvexa.studio</p>
      </div>
    </div>
  </section>

</body>
</html>
```